Consulting company with focus on aviation needs

We need a new business card design for our company. The company consults with multiple players in the industry like manufacturers and airlines. It is also a supplier and an inter-company level. Given the targeted industry (aviation) it should be both kind of serious, sound, secure, classy, ​​but also a bit technical, innovative. Should not be too playful, however, "fresh", "airy", "ligth" and "suprising" are suitabe attributes. The existing logo shall be used.

Industry/Entity Type

Airlines

```html
<!DOCTYPE html>
<html lang="en">
<head>
<meta charset="utf-8">
<title>Veltaro Business Card</title>
<link href="https://fonts.googleapis.com/css2?family=Work+Sans:wght@400;500;600&family=Saira+Semi+Condensed:wght@500&display=swap" rel="stylesheet">
<style>
  :root {
    --bg: #1b1b1b;
    --card-white: #ffffff;
    --teal: #1a9e80;
    --orange: #f0962a;
    --gray: #6b6b6b;
    --text: #555555;
  }
  * { margin: 0; padding: 0; box-sizing: border-box; }
  html, body { width: 1200px; height: 897px; overflow: hidden; background: var(--bg); }
  body { position: relative; font-family: "Work Sans", Arial, sans-serif; }

  .card {
    position: absolute;
    left: 303px;
    width: 594px;
    height: 339px;
    border-radius: 21px;
    overflow: hidden;
  }
  .card--front { top: 92px; background: var(--card-white); }
  .card--back { top: 469px; background: var(--teal); }

  /* Front: brand block */
  .brand {
    position: absolute;
    left: 0;
    top: 0;
    width: 331px;
    height: 339px;
  }
  .brand__dot {
    position: absolute;
    left: 150px;
    top: 96px;
    width: 76px;
    height: 76px;
    border-radius: 50%;
    background: var(--teal);
  }
  .brand__name {
    position: absolute;
    left: 0;
    width: 331px;
    top: 189px;
    text-align: center;
    font-weight: 600;
    font-size: 39px;
    letter-spacing: 0.16em;
    color: var(--gray);
    line-height: 1;
    padding-left: 46px;
  }
  .brand__tagline {
    position: absolute;
    left: 0;
    width: 331px;
    top: 228px;
    text-align: center;
    padding-left: 40px;
    font-family: "Saira Semi Condensed", Arial, sans-serif;
    font-weight: 500;
    font-size: 15px;
    color: var(--orange);
    white-space: nowrap;
  }

  .divider {
    position: absolute;
    left: 331px;
    top: 78px;
    width: 2px;
    height: 180px;
    background: var(--orange);
  }

  /* Front: contact block */
  .contact { position: absolute; left: 355px; top: 72px; color: var(--text); }
  .contact__name {
    font-weight: 500;
    font-size: 25px;
    color: var(--teal);
    letter-spacing: 0.02em;
    line-height: 1.2;
  }
  .contact__role { font-size: 14px; margin-top: 2px; }
  .contact__address { font-size: 14px; line-height: 1.25; margin-top: 20px; padding-left: 2px; letter-spacing: 0.02em; }
  .contact__list { list-style: none; margin-top: 19px; }
  .contact__item {
    display: flex;
    align-items: center;
    font-size: 14px;
    height: 19.3px;
    letter-spacing: 0.02em;
  }
  .contact__icon { width: 11px; height: 11px; margin-right: 9px; flex: none; }
  .contact__accent { color: var(--teal); }

  /* Back */
  .back__pattern { position: absolute; inset: 0; width: 100%; height: 100%; }
  .back__content {
    position: absolute;
    left: 0;
    width: 100%;
    top: 138px;
    text-align: center;
    color: #ffffff;
  }
  .back__name {
    font-weight: 600;
    font-size: 42px;
    letter-spacing: 0.2em;
    padding-left: 0.2em;
    line-height: 1;
  }
  .back__tagline {
    font-family: "Saira Semi Condensed", Arial, sans-serif;
    font-weight: 500;
    font-size: 16px;
    margin-top: 6px;
    white-space: nowrap;
  }
  .back__url {
    font-size: 16px;
    letter-spacing: 0.55em;
    margin-top: 8px;
    padding-left: 0.55em;
  }
</style>
</head>
<body>
  <section class="card card--front">
    <div class="brand">
      <div class="brand__dot"></div>
      <div class="brand__name">VELTARO</div>
      <div class="brand__tagline">Linking Partners - Shaping Flight</div>
    </div>
    <div class="divider"></div>
    <div class="contact">
      <h1 class="contact__name">DANIEL HART</h1>
      <p class="contact__role">Founder</p>
      <p class="contact__address">48 Harbor Lane, Suite<br>310, Fairview OR 97024</p>
      <ul class="contact__list">
        <li class="contact__item">
          <svg class="contact__icon" viewBox="0 0 12 12"><path fill="#1a9e80" d="M2.4 0.6 4.3 2.5 3.4 4a7 7 0 0 0 4.6 4.6l1.5-0.9 1.9 1.9-1.3 1.8C5 11 1 7 0.6 1.9z"/></svg>
          800-555-0147
        </li>
        <li class="contact__item">
          <svg class="contact__icon" viewBox="0 0 12 12"><rect x="3" y="0.5" width="6" height="11" rx="1" fill="none" stroke="#1a9e80" stroke-width="1.3"/><rect x="5" y="9" width="2" height="1" fill="#1a9e80"/></svg>
          310-555-0198
        </li>
        <li class="contact__item">
          <svg class="contact__icon" viewBox="0 0 12 12"><rect x="0.5" y="2" width="11" height="8" fill="#1a9e80"/><path d="M0.5 2 6 6.5 11.5 2" fill="none" stroke="#fff" stroke-width="1.1"/></svg>
          info@veltaro.com
        </li>
        <li class="contact__item">
          <svg class="contact__icon" viewBox="0 0 12 12" fill="none" stroke="#1a9e80" stroke-width="1"><circle cx="6" cy="6" r="5.2"/><ellipse cx="6" cy="6" rx="2.3" ry="5.2"/><path d="M0.8 6h10.4M1.6 3.4h8.8M1.6 8.6h8.8"/></svg>
          www.<span class="contact__accent">veltaro</span>.com
        </li>
      </ul>
    </div>
  </section>

  <section class="card card--back">
    <svg class="back__pattern" role="img" aria-label="Faint repeating pattern of brand marks across the card" viewBox="0 0 594 339" preserveAspectRatio="none">
      <rect width="594" height="339" fill="#1a9e80"/>
    </svg>
    <div class="back__content">
      <div class="back__name">VELTARO</div>
      <div class="back__tagline">Linking Partners - Shaping Flight</div>
      <div class="back__url">www.veltaro.com</div>
    </div>
  </section>
</body>
</html>
```